Silver Heron Construction Services

Create a business card for my business consulting company
Danielle Vesk, Founder and CEO
4816 Alder Brook Way, Ste 100
Denver, CO. 80451
303.782.4190 cell
dvesk@silverheronconst.example
www.silverheronconst.example

Target Market(s)

Private Equity and Construction Companies

Industry/Entity Type

Business / Sales Consulting

Contact Information for Business Card

Tag Line that says "Where The Road To Success Is Always Under Construction"

Requirements
Must have
• Logo on both sides of the card.
Nice to have
• Add tagline to the same side of the card as my name and contact info

```html
<!DOCTYPE html>
<html lang="en">
<head>
<meta charset="UTF-8">
<title>Silver Heron Construction Services – Business Card</title>
<link href="https://fonts.googleapis.com/css2?family=Montserrat:wght@400;600&family=Roboto:wght@500;700&display=swap" rel="stylesheet">
<style>
  :root {
    --page-bg: #f1f1f4;
    --card-navy: #1b1a3a;
    --card-navy-deep: #15142f;
    --ghost-navy: #25244a;
    --ink-white: #ffffff;
    --ink-soft: #d9d9e3;
    --ink-muted: #8d8ca3;
    --card-w: 900px;
    --card-h: 514px;
  }
  * { margin: 0; padding: 0; box-sizing: border-box; }
  html, body {
    width: 1200px; height: 1200px; overflow: hidden;
    background: var(--page-bg);
  }
  .sheet { position: relative; width: 1200px; height: 1200px; }

  .card {
    position: absolute; left: 150px;
    width: var(--card-w); height: var(--card-h);
    background: linear-gradient(135deg, var(--card-navy) 0%, var(--card-navy-deep) 100%);
    overflow: hidden;
    box-shadow: 0 10px 26px rgba(20, 20, 40, 0.25);
  }
  .card--front { top: 48px; }
  .card--back { top: 638px; }

  /* brand wordmark */
  .brand {
    position: absolute; display: flex; align-items: center; gap: 12px;
    font-family: "Montserrat", sans-serif; font-weight: 600;
    color: var(--ink-white); text-transform: uppercase;
  }
  .brand__dot {
    width: 22px; height: 22px; border-radius: 50%;
    background: var(--ink-white); flex: none;
  }
  .brand__text { display: flex; flex-direction: column; line-height: 1.15; }
  .brand__name { font-size: 30px; letter-spacing: 1px; }
  .brand__sub { font-size: 11px; letter-spacing: 3px; }

  .brand-ghost {
    position: absolute;
    font-family: "Montserrat", sans-serif; font-weight: 600;
    color: var(--ghost-navy); text-transform: uppercase;
    line-height: 1.1; white-space: nowrap;
  }
  .brand-ghost__name { font-size: 74px; letter-spacing: 2px; }
  .brand-ghost__sub { font-size: 26px; letter-spacing: 9px; }

  /* front */
  .card--front .brand-ghost { left: 110px; top: 140px; }
  .card--front .brand { left: 50%; top: 180px; transform: translateX(-50%); }
  .tagline {
    position: absolute; left: 0; right: 0; top: 345px;
    text-align: center;
    font-family: "Roboto", sans-serif; font-weight: 700;
    font-size: 22px; color: var(--ink-soft); letter-spacing: 0.3px;
  }

  /* back */
  .card--back .brand-ghost { left: 40px; top: 150px; }
  .card--back .brand { left: 70px; top: 220px; }
  .brand--compact .brand__name { font-size: 24px; }
  .brand--compact .brand__sub { font-size: 9px; letter-spacing: 2.4px; }

  .contact {
    position: absolute; left: 468px; top: 112px;
    font-family: "Montserrat", sans-serif; color: var(--ink-white);
  }
  .contact__person {
    border-left: 4px solid var(--ink-white);
    padding-left: 14px; margin-bottom: 26px;
  }
  .contact__name {
    font-family: "Roboto", sans-serif; font-weight: 700;
    font-size: 30px; line-height: 1.15;
  }
  .contact__role {
    font-family: "Roboto", sans-serif; font-weight: 500;
    font-size: 17px; color: var(--ink-muted);
  }
  .contact__list { list-style: none; padding-left: 22px; }
  .contact__item {
    display: flex; align-items: flex-start; gap: 16px;
    font-size: 20px; line-height: 1.35; margin-bottom: 14px;
  }
  .contact__icon {
    width: 28px; height: 28px; flex: none; margin-top: 1px;
    border-radius: 50%; background: var(--ink-white);
    display: flex; align-items: center; justify-content: center;
  }
  .contact__icon svg { width: 16px; height: 16px; }
</style>
</head>
<body>
<main class="sheet">

  <section class="card card--front" aria-label="Card front">
    <div class="brand-ghost" aria-hidden="true">
      <div class="brand-ghost__name">Silver Heron</div>
      <div class="brand-ghost__sub">Construction Services</div>
    </div>
    <div class="brand">
      <span class="brand__dot"></span>
      <span class="brand__text">
        <span class="brand__name">Silver Heron</span>
        <span class="brand__sub">Construction Services</span>
      </span>
    </div>
    <p class="tagline">Where The Road To Success Is Always Under Construction</p>
  </section>

  <section class="card card--back" aria-label="Card back">
    <div class="brand-ghost" aria-hidden="true">
      <div class="brand-ghost__name">Silver Heron</div>
      <div class="brand-ghost__sub">Construction Services</div>
    </div>
    <div class="brand brand--compact">
      <span class="brand__dot"></span>
      <span class="brand__text">
        <span class="brand__name">Silver Heron</span>
        <span class="brand__sub">Construction Services</span>
      </span>
    </div>

    <div class="contact">
      <div class="contact__person">
        <div class="contact__name">Danielle Vesk</div>
        <div class="contact__role">Founder and CEO</div>
      </div>
      <ul class="contact__list">
        <li class="contact__item">
          <span class="contact__icon">
            <svg viewBox="0 0 24 24"><path fill="#1b1a3a" d="M6.6 10.8a15.1 15.1 0 0 0 6.6 6.6l2.2-2.2a1 1 0 0 1 1-.25 11.4 11.4 0 0 0 3.6.57 1 1 0 0 1 1 1V20a1 1 0 0 1-1 1A17 17 0 0 1 3 4a1 1 0 0 1 1-1h3.5a1 1 0 0 1 1 1c0 1.25.2 2.45.57 3.57a1 1 0 0 1-.25 1z"/></svg>
          </span>
          <span>303 782 4190</span>
        </li>
        <li class="contact__item">
          <span class="contact__icon">
            <svg viewBox="0 0 24 24"><rect x="3" y="6" width="18" height="12" rx="1.5" fill="none" stroke="#1b1a3a" stroke-width="2"/><path d="M3.5 7 12 13l8.5-6" fill="none" stroke="#1b1a3a" stroke-width="2"/></svg>
          </span>
          <span>dvesk@silverheronconst.example</span>
        </li>
        <li class="contact__item">
          <span class="contact__icon">
            <svg viewBox="0 0 24 24"><g fill="none" stroke="#1b1a3a" stroke-width="2"><circle cx="12" cy="12" r="9"/><path d="M3 12h18M12 3c3 3 3 15 0 18M12 3c-3 3-3 15 0 18"/></g></svg>
          </span>
          <span>www.silverheronconst.example</span>
        </li>
        <li class="contact__item">
          <span class="contact__icon">
            <svg viewBox="0 0 24 24"><path fill="#1b1a3a" d="M12 2a7 7 0 0 0-7 7c0 5.2 7 13 7 13s7-7.8 7-13a7 7 0 0 0-7-7zm0 9.5A2.5 2.5 0 1 1 12 6.5a2.5 2.5 0 0 1 0 5z"/></svg>
          </span>
          <span>4816 Alder Brook Way,<br>Ste 100<br>Denver, CO. 80451</span>
        </li>
      </ul>
    </div>
  </section>

</main>
</body>
</html>
```